integrative health clinic-Medical massage, acupuncture, chiropractic

we like our logo, but are open to new ideas. We need a new card design. We have added chiropractic and acupuncture that we have put under the name of the business. We are an integrative medical clinic

Target Market(s)

General public, athletes

Contact Information for Business Card

Phone 5055583927
Fax 5055583926
Hours Monday-Friday 9-6
Saturday 10-6
The 20% can be smaller on the back

Colors
3176b5
0355a3

Requirements
Must have
• Logo but am open to ideas
Nice to have
• We are an integrated medical clinic but also want to be personable. We want the card fun and inviting

```html
<!DOCTYPE html>
<html lang="en">
<head>
<meta charset="utf-8">
<title>Full Circle Wellness – Business Card</title>
<link rel="stylesheet" href="https://fonts.googleapis.com/css2?family=Montserrat:wght@400;700&family=Roboto+Condensed:wght@400;700&family=Roboto+Slab:wght@700&family=Roboto:wght@400&display=swap">
<style>
  :root {
    --brand-blue: #0d55a1;
    --brand-light: #3176b5;
    --paper: #ffffff;
    --backdrop: #f5f5f5;
    --shadow: rgba(0, 0, 0, 0.28);
  }
  * { margin: 0; padding: 0; box-sizing: border-box; }
  html, body {
    width: 1200px; height: 1154px; overflow: hidden;
    background: var(--backdrop);
  }
  .canvas { position: relative; width: 1200px; height: 1154px; }

  .card {
    position: absolute;
    box-shadow: 14px 16px 22px var(--shadow);
    overflow: hidden;
  }

  /* Front */
  .card-front {
    left: 42px; top: 424px; width: 508px; height: 306px;
    background: var(--paper);
  }
  .brand {
    position: absolute; left: 0; right: 0; text-align: center;
  }
  .front-brand { top: 58px; }
  .brand-dot {
    display: block; margin: 0 auto 14px;
    width: 20px; height: 20px; border-radius: 50%;
    background: var(--brand-light);
  }
  .brand-name {
    font-family: "Roboto Slab", serif; font-weight: 700;
    font-size: 19px; color: var(--brand-blue); line-height: 1.2;
  }
  .brand-tagline {
    font-family: "Roboto", sans-serif; font-weight: 400;
    font-size: 11.5px; color: var(--brand-blue); margin-top: 3px;
  }
  .info-band {
    position: absolute; left: 0; right: 0; top: 187px; bottom: 0;
    background: var(--brand-blue); color: var(--paper);
    font-family: "Montserrat", sans-serif; font-size: 9.5px;
  }
  .info-grid {
    position: absolute; top: 14px; line-height: 15px;
    display: grid; column-gap: 6px;
  }
  .hours { left: 49px; grid-template-columns: 34px 82px auto; }
  .contact { left: 358px; grid-template-columns: 34px auto; }
  .info-grid .label { font-weight: 700; }
  .band-rule {
    position: absolute; left: 0; right: 0; top: 54px;
    height: 1px; background: var(--paper);
  }
  .email {
    position: absolute; left: 0; right: 0; top: 68px;
    text-align: center; font-size: 12.5px; letter-spacing: 0.2px;
  }

  /* Back */
  .card-back {
    left: 652px; top: 420px; width: 506px; height: 310px;
    background: var(--brand-blue); color: var(--paper);
  }
  .frame {
    position: absolute; inset: 17px; border: 1.5px solid var(--paper);
  }
  .frame-inner {
    position: absolute; inset: 23px; border: 1.5px solid var(--paper);
  }
  .back-brand { top: 44px; }
  .back-brand .brand-dot { background: var(--paper); width: 16px; height: 16px; margin-bottom: 12px; }
  .back-brand .brand-name { color: var(--paper); font-size: 14px; }
  .back-brand .brand-tagline { color: var(--paper); font-size: 8px; margin-top: 2px; }
  .offer {
    position: absolute; left: 0; right: 0; top: 150px; text-align: center;
    font-family: "Roboto Condensed", sans-serif; font-weight: 700;
    font-size: 24px; letter-spacing: -0.3px;
  }
  .book-online {
    position: absolute; left: 0; right: 0; top: 258px; text-align: center;
    font-family: "Roboto Condensed", sans-serif; font-weight: 400;
    font-size: 13px;
  }
</style>
</head>
<body>
<div class="canvas">

  <section class="card card-front" aria-label="Business card front">
    <div class="brand front-brand">
      <span class="brand-dot"></span>
      <div class="brand-name">Full Circle Wellness</div>
      <div class="brand-tagline">Sports Therapy and Wellness Center</div>
    </div>
    <div class="info-band">
      <div class="info-grid hours">
        <span class="label">Hours</span><span>: Monday-Friday :</span><span>9.00 AM - 6.00 PM</span>
        <span></span><span>&nbsp;&nbsp;Saturday</span><span>: 10.00 AM - 6.00 PM</span>
      </div>
      <div class="info-grid contact">
        <span class="label">Phone</span><span>: &nbsp;5055583927</span>
        <span class="label">Fax</span><span>: &nbsp;5055583926</span>
      </div>
      <div class="band-rule"></div>
      <div class="email">info@fullcirclewellnessnm.com</div>
    </div>
  </section>

  <section class="card card-back" aria-label="Business card back">
    <div class="frame"></div>
    <div class="frame-inner"></div>
    <div class="brand back-brand">
      <span class="brand-dot"></span>
      <div class="brand-name">Full Circle Wellness</div>
      <div class="brand-tagline">Sports Therapy and Wellness Center</div>
    </div>
    <div class="offer">20 % OFF FIRST VISIT</div>
    <div class="book-online">book online : www.fullcirclewellnessnm.com</div>
  </section>

</div>
</body>
</html>
```